Professional Home Buyer business card needed

I need a pretty straight forward business card designed. We help people that NEED to sell their homes solve problems. We perform all types of Real Estate transactions including flip, wholesale, investment, rental property and multi family. The card will mainly be used to give to prospective Sellers but will also be given to Real Estate Investors as well. It should professional and very easy to read, most clients are older people.

Target Market(s)

Distressed home sellers as well as Real Estate investors

Industry/Entity Type

Real Estate

Contact Information for Business Card

should be a professional layout

Colors
ec1f27
ffffff
000000

Requirements
Must have
• Large logo on back and smaller one on front. should utilize Red, white, and black.
• I am thinking of using a soft touch coating on the card so keep that in mind.
• Contact info should be very easy to read, think older clients.
Nice to have
• I would like to see a design with rounded corners on the card
Should not have
• pictures of homes or other home graphics.

```html
<!DOCTYPE html>
<html lang="en">
<head>
<meta charset="utf-8">
<title>Summit Home Buyers – Business Card</title>
<link href="https://fonts.googleapis.com/css2?family=Montserrat:wght@400;500;600;700;800&display=swap" rel="stylesheet">
<style>
  :root {
    --brand-red: #ec1f27;
    --ink: #2b2b2b;
    --muted: #555555;
    --card-dark: #3a3c3f;
    --card-light: #ffffff;
    --stage: #262626;
  }
  * { box-sizing: border-box; margin: 0; padding: 0; }
  html, body { width: 1200px; height: 716px; overflow: hidden; }
  body {
    background: var(--stage);
    font-family: "Montserrat", sans-serif;
    position: relative;
  }
  .card {
    position: absolute;
    top: 210px;
    width: 520px;
    height: 297px;
    border-radius: 14px;
  }
  .card--back {
    left: 50px;
    background: var(--card-dark);
    display: flex;
    align-items: center;
    justify-content: center;
  }
  .card--back .brand-name {
    color: var(--card-light);
    font-weight: 800;
    font-size: 40px;
    letter-spacing: 1px;
    text-transform: uppercase;
    text-align: center;
    line-height: 1.1;
  }
  .card--front {
    left: 630px;
    background: var(--card-light);
    display: flex;
    align-items: center;
    padding: 0 30px;
  }
  .front-brand {
    width: 175px;
    color: var(--ink);
    font-weight: 800;
    font-size: 22px;
    letter-spacing: 0.5px;
    text-transform: uppercase;
    line-height: 1.15;
  }
  .divider {
    width: 2px;
    height: 190px;
    background: var(--brand-red);
    margin: 0 22px 0 18px;
  }
  .contact { color: var(--ink); }
  .contact__name {
    color: var(--brand-red);
    font-weight: 600;
    font-size: 22px;
    line-height: 1.1;
  }
  .contact__title {
    color: var(--muted);
    font-size: 17px;
    margin-bottom: 12px;
  }
  .contact__address {
    font-size: 14px;
    line-height: 1.4;
    color: var(--muted);
    margin-bottom: 10px;
  }
  .contact__row {
    display: flex;
    align-items: center;
    gap: 8px;
    font-size: 13.5px;
    line-height: 1.65;
    color: var(--muted);
  }
  .contact__row svg { width: 14px; height: 14px; flex: none; }
</style>
</head>
<body>
  <section class="card card--back">
    <div class="brand-name">Summit<br>Home Buyers</div>
  </section>

  <section class="card card--front">
    <div class="front-brand">Summit<br>Home Buyers</div>
    <div class="divider"></div>
    <div class="contact">
      <p class="contact__name">Daniel Marsh</p>
      <p class="contact__title">President</p>
      <p class="contact__address">P.O. Box 218<br>Millbrook, KS 67110</p>
      <p class="contact__row">
        <svg viewBox="0 0 24 24" aria-hidden="true"><path fill="#ec1f27" d="M6.6 10.8a15.1 15.1 0 0 0 6.6 6.6l2.2-2.2c.3-.3.7-.4 1-.2 1.1.4 2.3.6 3.6.6.6 0 1 .4 1 1V20c0 .6-.4 1-1 1A17 17 0 0 1 3 4c0-.6.4-1 1-1h3.5c.6 0 1 .4 1 1 0 1.3.2 2.5.6 3.6.1.3 0 .7-.2 1z"/></svg>
        316-555-0148
      </p>
      <p class="contact__row">
        <svg viewBox="0 0 24 24" aria-hidden="true"><rect x="2" y="5" width="20" height="14" rx="1" fill="#ec1f27"/><path d="M2 6l10 7 10-7" fill="none" stroke="#fff" stroke-width="1.6"/></svg>
        dan@plainshomesforcash.com
      </p>
      <p class="contact__row">
        <svg viewBox="0 0 24 24" aria-hidden="true"><g fill="none" stroke="#ec1f27" stroke-width="1.8"><circle cx="12" cy="12" r="9.5"/><ellipse cx="12" cy="12" rx="4" ry="9.5"/><path d="M2.5 12h19M4 7h16M4 17h16"/></g></svg>
        www.plainshomesforcash.com
      </p>
    </div>
  </section>
</body>
</html>
```